Modern Web Design for Nonprofit Organization

Our client is looking to redesign their website. They want a modern look, clean and professional, that integrates their new brand guidelines.

Here is clients current site:
http://www.valorandes.org/

They want their own unique design but here are some sites the clients likes:
https://www.brixtonvane.com/en/
https://oakhollowrise.org/
https://www.lumacraft.com/
https://www.tbnlawgroup.com/
https://www.greyharborco.org/

Attached please find the clients logos, color palette, site plan and design specs.

You will create a homepage mockup that will have the following sections in this order:
1. Thin Alert Bar at very top with one line message
2. Nav Bar with Logo and Main Nav (red in site plan)
3. Hero Image or Video
4. Signup Bar with name email and zip and connect button
5. Intro section with image, welcome message, and supporter counter
6. Featured Action section with call to action
7. Event section with two upcoming event cards
8. Latest News section with three latest blog post
9. Support our work (donation) section
10. Worker and Member Stories Section with feed of social posts
11. Footer.

You can use text and images from clients existing site or placeholder images and placeholder text.

Please submit as many home page mockups/idea boards as you like. Client will pick the top three and ask for some revisions. If you are selected this will lead to a lot of work for this client.

Project is private please adhere to ArtPlenary terms of use and do not share any materials please.

QUICKEST RESPONSE PLEASE!

Thanks for looking!

Target Market(s)

Non profit donors and farmworker advocates

Number of Pages Required

2 page

Font styles to use
Sans Serif

Requirements
Must have
• Adhere to brief and client brand ID
Nice to have
• World class design

```html
<!DOCTYPE html>
<html lang="en">
<head>
<meta charset="utf-8">
<title>VAF Foundation</title>
<link href="https://fonts.googleapis.com/css2?family=Poppins:wght@300;400;500;600;700;800&family=Tinos&display=swap" rel="stylesheet">
<style>
:root{
  --red:#e01a1a;
  --teal:#14969a;
  --alert:#f9e3a8;
  --ink:#1b1b1b;
  --body:#444;
  --grey:#efefef;
  --dark:#232323;
  --ring:#b9c9c9;
}
*{margin:0;padding:0;box-sizing:border-box}
html,body{width:1200px;height:3832px;overflow:hidden}
body{font-family:'Poppins',sans-serif;color:var(--ink);background:#fff;position:relative}
.abs{position:absolute}
.alert-bar{left:0;top:0;width:1200px;height:28px;background:var(--alert);font-family:'Tinos',serif;font-size:10px;color:#6b5a2a;text-align:center;line-height:28px}
.header{left:0;top:28px;width:1200px;height:78px;background:#fff}
.brand{left:131px;top:14px;display:flex;align-items:center;gap:10px}
.brand-dot{width:56px;height:56px;border-radius:50%;background:var(--red)}
.brand-name{font-weight:700;font-size:20px;line-height:21px;color:var(--ink)}
.util{top:30px;font-size:14px;font-weight:500;color:var(--ink);display:flex;align-items:center;gap:6px}
.donate-btn{left:904px;top:17px;width:162px;height:46px;border-radius:23px;background:var(--red);color:#fff;font-weight:600;font-size:15px;text-align:center;line-height:46px}
.main-nav{left:0;top:106px;width:1200px;height:47px;background:var(--teal)}
.main-nav span{position:absolute;top:13px;font-family:'Tinos',serif;font-size:17px;color:#fff}
.main-nav span.drop::after{content:"";display:inline-block;width:6px;height:6px;border-right:1px solid #fff;border-bottom:1px solid #fff;transform:rotate(45deg);margin:0 0 4px 7px}
.hero{left:0;top:153px;width:1200px;height:595px;background:linear-gradient(180deg,#4c5b3c 0%,#5b6a48 45%,#3d3c3a 100%)}
.hero-kicker{left:131px;top:322px;font-size:27px;font-weight:400;color:#fff}
.hero-title{left:131px;top:372px;font-size:50px;font-weight:800;line-height:56px;color:#fff}
.watch{left:131px;top:507px;display:flex;align-items:center;gap:14px;color:#fff;font-weight:700;font-size:17px}
.play{width:58px;height:58px;border-radius:50%;background:var(--red);display:flex;align-items:center;justify-content:center}
.signup{left:691px;top:230px;width:375px;height:414px;background:#fff;padding:68px 53px 0}
.signup h3{font-size:21px;font-weight:600;margin-bottom:28px}
.field{height:40px;border-radius:20px;background:#eeeeee;font-size:14px;color:#888;padding-left:26px;line-height:40px;margin-bottom:18px}
.join{height:40px;border-radius:20px;background:var(--teal);color:#fff;text-align:center;line-height:40px;font-size:15px;font-weight:500}
.about-glow{left:0;top:748px;width:600px;height:538px;background:radial-gradient(ellipse at 40% 0%,#ececec 0%,#fff 55%)}
h2.section-title{font-weight:700;font-size:40px;line-height:50px;color:var(--ink)}
.copy{font-size:17px;line-height:26px;color:var(--body);letter-spacing:.2px}
.outline-btn{display:inline-block;border:2.5px solid var(--ink);border-radius:26px;height:48px;padding:0 28px;line-height:43px;font-weight:600;font-size:16px}
.photo-ring{border-radius:50%;border:5px solid var(--ring);padding:7px;background:#fff}
.photo-ring div{width:100%;height:100%;border-radius:50%}
.events{left:0;top:1286px;width:1200px;height:605px;background:var(--grey)}
.center-title{width:1200px;left:0;text-align:center;font-weight:700;font-size:38px}
.event-card{top:1420px;width:395px;height:384px;background:#fff}
.event-card .pic{height:217px}
.event-card h4{margin:30px 24px 12px;font-size:23px;font-weight:600}
.event-card p{margin:0 24px;font-size:17px;line-height:28px;color:var(--body)}
.news-card{top:2019px;width:293px;height:382px;background:#fff;box-shadow:0 2px 10px rgba(0,0,0,.08)}
.news-card .pic{height:173px}
.news-card .body{padding:18px 32px}
.news-date{color:var(--red);font-weight:600;font-size:15px}
.news-card h5{font-size:15.5px;font-weight:600;line-height:22px;margin:12px 0 10px}
.news-card p{font-size:13.5px;line-height:19px;color:var(--body)}
.more{color:var(--red);font-weight:600;font-size:14px;margin-top:12px}
.support{left:0;top:2476px;width:1200px;height:431px;overflow:hidden;background:linear-gradient(90deg,#e0211c,#d2241f)}
.support-teal{left:644px;top:-380px;width:1100px;height:1100px;border-radius:50%;background:#1c9a97}
.support-mark{left:805px;top:110px;width:200px;height:200px;border-radius:50%;background:#111}
.white-btn{display:inline-block;border:2.5px solid #fff;border-radius:26px;height:48px;padding:0 36px;line-height:43px;color:#fff;font-weight:600;font-size:16px}
.footer{left:0;top:3465px;width:1200px;height:285px;background:var(--dark);color:#fff}
.footer h6{font-size:19px;font-weight:500;margin-bottom:12px}
.footer .line{font-size:13.5px;color:#ddd;display:flex;gap:12px;align-items:flex-start;line-height:21px}
.footer .link{font-size:13.5px;color:#ddd;height:33px}
.footer .link::before{content:"";display:inline-block;width:6px;height:6px;border-radius:50%;background:var(--teal);margin-right:9px;vertical-align:middle}
.social{width:32px;height:32px;border-radius:50%;border:1.5px solid var(--teal)}
.copyright{left:0;top:3750px;width:1200px;height:82px;text-align:center;line-height:82px;font-size:13px;color:#555}
</style>
</head>
<body>

<div class="abs alert-bar">Lorem Ipsum is simply dummy text of the printing and typesetting industry. Lorem Ipsum has been the industry's standard dummy text ever since...</div>

<header class="abs header">
  <div class="abs brand"><div class="brand-dot"></div><div class="brand-name">VAF<br>FOUNDATION</div></div>
  <div class="abs util" style="left:655px">
    <svg width="15" height="16" viewBox="0 0 15 16" fill="none" stroke="#e01a1a" stroke-width="1.6"><circle cx="7.5" cy="5" r="3.8"/><path d="M1 15.5c0-4 3-6 6.5-6s6.5 2 6.5 6"/></svg>MEMBERSHIP</div>
  <div class="abs util" style="left:797px">
    <svg width="17" height="17" viewBox="0 0 17 17" fill="none" stroke="#e01a1a" stroke-width="1.6"><circle cx="8.5" cy="8.5" r="7.5"/><path d="M5 8.5h7M9 5.5l3 3-3 3"/></svg>LOGIN</div>
  <div class="abs donate-btn">DONATE</div>
</header>

<nav class="abs main-nav">
  <span style="left:147px">Home</span>
  <span class="drop" style="left:230px">Get Help</span>
  <span class="drop" style="left:340px">Take Action</span>
  <span class="drop" style="left:474px">News &amp; Events</span>
  <span class="drop" style="left:630px">Support</span>
  <span class="drop" style="left:736px">Our Work</span>
  <span class="drop" style="left:855px">About Us</span>
  <span style="left:970px">Contact Us</span>
</nav>

<section class="abs hero" role="img" aria-label="Group of people in a park holding joined hands raised together"></section>
<div class="abs hero-kicker">Welcome To VAF Foundation</div>
<h1 class="abs hero-title">Join The Peasant<br>Movement</h1>
<div class="abs watch"><div class="play"><svg width="18" height="20" viewBox="0 0 18 20"><path d="M2 1l15 9-15 9z" fill="#fff"/></svg></div>WATCH THE OVERVIEW</div>

<form class="abs signup">
  <h3>STAY INFORMED</h3>
  <div class="field">Name*</div>
  <div class="field">Email *</div>
  <div class="field">Zip/Postal Code *</div>
  <div class="join">Join Now</div>
</form>

<section>
  <div class="abs about-glow"></div>
  <h2 class="abs section-title" style="left:131px;top:852px">ABOUT<br>VAF FOUNDATION</h2>
  <p class="abs copy" style="left:130px;top:967px;width:460px">Lorem Ipsum is simply dummy text of the printing and typesetting industry. Lorem Ipsum has been</p>
  <p class="abs copy" style="left:130px;top:1033px;width:470px">industry's standard dummy text ever since the 1500s, when an unknown printer took a galley of type and scrambled Lorem Ipsum is simply dummy text of the printing and typesetting industry.</p>
  <div class="abs outline-btn" style="left:130px;top:1161px">LEARN MORE</div>
  <div class="abs photo-ring" style="left:647px;top:796px;width:430px;height:430px"><div role="img" aria-label="Circle of people raising joined hands outdoors" style="background:linear-gradient(160deg,#5d7748,#3c5630 60%,#2b3a2a)"></div></div>
</section>

<section class="abs events"></section>
<h2 class="abs center-title" style="top:1344px">UPCOMING EVENT</h2>
<article class="abs event-card" style="left:180px">
  <div class="pic" role="img" aria-label="Crowd of people gathered at a community meal" style="background:linear-gradient(135deg,#4a5366,#7a6f63 60%,#3b3f4a)"></div>
  <h4>UPCOING EVENT</h4>
  <p>Lorem Ipsum is simply dummy text of the printing and typesetting industry. Lorem Ipsum has been</p>
</article>
<article class="abs event-card" style="left:625px">
  <div class="pic" role="img" aria-label="Group of young adults listening at an event" style="background:linear-gradient(135deg,#6f7c8f,#3e4c66 60%,#8b8579)"></div>
  <h4>UPCOING EVENT</h4>
  <p>Lorem Ipsum is simply dummy text of the printing and typesetting industry. Lorem Ipsum has been</p>
</article>

<h2 class="abs center-title" style="top:1946px">LATEST NEWS</h2>
<article class="abs news-card" style="left:131px">
  <div class="pic" role="img" aria-label="Hands flipping through a newspaper" style="background:linear-gradient(135deg,#8b7d70,#d9d6d2 60%,#a9a39c)"></div>
  <div class="body"><div class="news-date">JAN 20, 2020</div><h5>INDUSTRY'S STANDARD<br>DUMMY TEXT EVER</h5><p>Lorem Ipsum is simply dummy text of the printing &amp; typesetting industry. Lorem Ipsum</p><div class="more">LEARN MORE &#8250;</div></div>
</article>
<article class="abs news-card" style="left:452px">
  <div class="pic" role="img" aria-label="Woman reading outdoors in sunlit greenery" style="background:linear-gradient(135deg,#8fb65a,#d8e0b0 55%,#5d8a3a)"></div>
  <div class="body"><div class="news-date">JAN 20, 2020</div><h5>INDUSTRY'S STANDARD<br>DUMMY TEXT EVER</h5><p>Lorem Ipsum is simply dummy text of the printing &amp; typesetting industry. Lorem Ipsum</p><div class="more">LEARN MORE &#8250;</div></div>
</article>
<article class="abs news-card" style="left:775px">
  <div class="pic" role="img" aria-label="People holding hands in a park" style="background:linear-gradient(135deg,#5c7a4a,#8a8f84 55%,#3f4a3c)"></div>
  <div class="body"><div class="news-date">JAN 20, 2020</div><h5>INDUSTRY'S STANDARD<br>DUMMY TEXT EVER</h5><p>Lorem Ipsum is simply dummy text of the printing &amp; typesetting industry. Lorem Ipsum</p><div class="more">LEARN MORE &#8250;</div></div>
</article>

<section class="abs support" role="img" aria-label="Tinted photo of people celebrating with raised hands">
  <div class="abs support-teal"></div>
  <div class="abs support-mark"></div>
  <h2 class="abs" style="left:174px;top:116px;font-size:38px;font-weight:700;color:#fff">SUPPORT OUR WORK</h2>
  <p class="abs" style="left:174px;top:174px;width:420px;font-size:16px;line-height:23px;color:#fff">Lorem Ipsum is simply dummy text of the printing &amp; typesetting industry. Lorem Ipsum</p>
  <div class="abs white-btn" style="left:174px;top:248px">DONATE NOW</div>
</section>

<section>
  <div class="abs photo-ring" style="left:133px;top:2967px;width:430px;height:430px"><div role="img" aria-label="Smiling older couple looking at a laptop together" style="background:linear-gradient(150deg,#c9c0b2,#8d8477 55%,#4b4c55)"></div></div>
  <h2 class="abs section-title" style="left:611px;top:3022px;font-size:36px">SHARE YOUR STORY</h2>
  <p class="abs copy" style="left:611px;top:3083px;width:470px">Lorem Ipsum is simply dummy text of the printing and typesetting industry. Lorem Ipsum has been</p>
  <p class="abs copy" style="left:611px;top:3150px;width:470px">industry's standard dummy text ever since the 1500s, when an unknown printer took a galley of type and scrambled Lorem Ipsum is simply dummy text of the printing and typesetting industry.</p>
  <div class="abs outline-btn" style="left:611px;top:3284px">LEARN MORE</div>
</section>

<footer class="abs footer">
  <div class="abs" style="left:181px;top:72px;width:102px;height:102px;border-radius:50%;background:var(--red)"></div>
  <div class="abs" style="left:153px;top:192px;display:flex;gap:6px"><div class="social"></div><div class="social"></div><div class="social"></div><div class="social"></div></div>
  <div class="abs" style="left:426px;top:70px">
    <h6>CONTACT INFO</h6>
    <div class="line"><svg width="13" height="17" viewBox="0 0 13 17"><path d="M6.5 0C3 0 0 2.8 0 6.3 0 11 6.5 17 6.5 17S13 11 13 6.3C13 2.8 10 0 6.5 0zm0 9a2.7 2.7 0 110-5.4 2.7 2.7 0 010 5.4z" fill="#aaa"/></svg><span>#123 Address, Street 25<br>Dummy Address</span></div>
    <div class="line" style="margin-top:14px"><svg width="15" height="15" viewBox="0 0 24 24"><path d="M6.6 10.8a15.1 15.1 0 006.6 6.6l2.2-2.2c.3-.3.7-.4 1-.2 1.1.4 2.3.6 3.6.6.6 0 1 .4 1 1V20c0 .6-.4 1-1 1C10.6 21 3 13.4 3 4c0-.6.4-1 1-1h3.5c.6 0 1 .4 1 1 0 1.3.2 2.5.6 3.6.1.3 0 .7-.2 1z" fill="#aaa"/></svg><span>+888 888 8888</span></div>
    <div class="line" style="margin-top:14px"><svg width="15" height="12" viewBox="0 0 15 12"><rect x=".5" y=".5" width="14" height="11" fill="none" stroke="#aaa"/><path d="M.5.5l7 6 7-6" fill="none" stroke="#aaa"/></svg><span>info@vaffoundation.org</span></div>
  </div>
  <div class="abs" style="left:730px;top:70px;width:320px">
    <h6>COMPANY</h6>
    <div style="display:grid;grid-template-columns:192px 128px">
      <div class="link">Home</div><div class="link">Support</div>
      <div class="link">Get Help</div><div class="link">Our Work</div>
      <div class="link">Take Action</div><div class="link">About Us</div>
      <div class="link">News &amp; Events</div><div class="link">Contact Us</div>
    </div>
  </div>
</footer>
<div class="abs copyright">© 2020 VAF Foundation. All Rights are Reserved.</div>

</body>
</html>
```